Redesign of tourdepays.com website (3 page types)

We need a fresh rebrush of www.tourdepays.com, a portal for french regions, departements and cities. It shall look modern as the current design is over 10 years old.

We like the blueish colors and the french touch (blue, white, red).

There are 3 page types that we currently need:
- Homepage (http://www.tourdepays.com/)
- Region overview (e.g. http://www.tourdepays.com/provence-alpes-cote-d-azur)
- City overview (e.g. http://www.tourdepays.com/provence-alpes-cote-d-azur/bouches-du-rhone/marseille)

See "Must have" for a more detailed briefing. All required elements exist and need a rebrush/redesign

Requirements
Must have
• General:

- 3 column layout
+ Header
+ Left sidebar
+ Content area
+ Right sidebar (250px inner width for ads)
+ Footer
- 3 classes of headlines
- Simple sidebar widgets (headline & content / without headline)

Header:
- Logo
- 2 or 3 links
- Search box
- Breadcrumb navigation

Footer:
- Nothing special, really

Homepage:
- Nice looking map with visible region borders to create a mouseover effect (as seen on current version). Meaning we need the plain map and a version with each region highlighted
- Text areas
- Content boxes (like the current gray ones)

Region overview
- Headline
- Info box (Informations)
- Mini map
- Crest / emblem
- Text area with headline for a long descriptive text with a "read more" / "show less" button/link to pop out the whole text via javascript
- List of the 24 biggest cities in the region

City overview
- Headline
- Info box (Informations, same look as for regions)
- Mini map
- List of the 24 cities nearby
- List of available photos
- Example sidebar widgets (right sidebar):
+ Upload a photo of this city
+ Weather conditions
+ Link list
Nice to have
• - A new favicon
- Facebook og:image
Should not have
• - Flash
- Animations

```html
<!DOCTYPE html>
<html lang="fr">
<head>
<meta charset="utf-8">
<title>tourdepays.com – portail de France</title>
<link rel="stylesheet" href="https://fonts.googleapis.com/css2?family=Noto+Sans:wght@400;700&family=PT+Sans:wght@400;700&display=swap">
<style>
:root{
  --navy:#14306e;
  --navy-dark:#0c1f52;
  --btn-top:#3a5cae;
  --btn-bottom:#1b3578;
  --red:#e3101f;
  --flag-blue:#0d2a78;
  --text:#222;
  --heading:#1c1c1c;
  --border:#d9d9d9;
  --white:#fff;
}
*{box-sizing:border-box;margin:0;padding:0}
html,body{width:1200px;height:898px;overflow:hidden;background:var(--white)}
body{position:relative;font-family:"Noto Sans",Verdana,sans-serif;color:var(--text)}
.abs{position:absolute}

/* header */
.hero{left:0;top:0;width:1200px;height:378px;
  background:linear-gradient(90deg,var(--flag-blue) 0,var(--flag-blue) 95px,transparent 140px,transparent 1060px,var(--red) 1110px),
  linear-gradient(180deg,#2a7fd0 0%,#79b6e8 30%,#e8eaa0 55%,#b7b436 70%,#5a6b40 85%,#606a70 100%)}
.hero-scene{left:100px;top:0;width:1000px;height:338px}
.logo{left:94px;top:50px;width:210px;color:var(--white);font-family:"PT Sans",sans-serif;font-weight:700;text-align:right}
.logo-name{font-size:31px;line-height:36px;display:block;text-align:left}
.logo-tag{font-size:16px;display:block;margin-top:-1px}
.top-links{left:622px;top:25px;font-family:"PT Sans",sans-serif;font-weight:700;font-size:15px;color:var(--navy)}
.top-links a{color:var(--navy);text-decoration:none}
.search{left:836px;top:20px;display:flex;gap:7px}
.search-field{width:190px;height:28px;background:var(--white);border:1px solid #ccc;font-size:11px;font-weight:700;color:var(--navy);padding:6px 9px}
.search-btn{width:37px;height:28px;background:var(--navy-dark);display:flex;align-items:center;justify-content:center}
.polaroid{background:#f4f2ec;padding:8px 8px 26px;box-shadow:2px 3px 8px rgba(0,0,0,.35)}
.polaroid div{width:100%;height:100%}

/* city strip */
.city-strip{left:114px;top:338px;width:982px;height:67px;background:var(--white);border-radius:6px 6px 0 0}
.city-rule{left:126px;top:405px;width:959px;height:5px;background:var(--red)}
.city{position:absolute;top:6px;width:70px;text-align:center;font-size:11px;line-height:13px;color:#111}
.crest{width:38px;height:42px;margin:0 auto 3px;border-radius:3px 3px 19px 19px}
.arrow{position:absolute;top:24px;width:0;height:0;border-top:6px solid transparent;border-bottom:6px solid transparent}

/* left sidebar */
.crumb{left:140px;top:414px;font-size:14px;color:var(--navy)}
.side-title{font-family:"PT Sans",sans-serif;font-weight:700;font-size:17px;color:var(--navy)}
.regions{left:149px;top:463px;display:flex;flex-direction:column;align-items:flex-start;gap:4px}
.region{display:inline-block;height:22px;line-height:22px;padding:0 7px;font-size:12.5px;color:var(--white);
  background:linear-gradient(var(--btn-top),var(--btn-bottom));box-shadow:2px 2px 2px rgba(0,0,0,.25)}

/* content */
.section-title{font-family:"PT Sans",sans-serif;font-weight:700;font-size:16px;color:var(--heading)}
.intro-box{left:345px;top:460px;width:478px;height:351px;border:1px solid var(--border);border-radius:5px}
.map{left:350px;top:520px;width:265px;height:272px;border-radius:40% 45% 35% 40%;
  background:radial-gradient(circle at 45% 45%,#f3c331 0,#ef7d28 30%,#d8306b 50%,#3a6bc4 70%,#7a4fb0 90%,transparent 100%)}
.intro-text{left:620px;top:463px;width:203px;font-size:11.4px;line-height:14px;letter-spacing:-.2px}
.intro-text p{margin-bottom:14px}
.feature-box{left:345px;top:848px;width:478px;height:70px;border:1px solid var(--navy);border-radius:5px;padding:4px 12px;font-size:11.4px;line-height:14px;letter-spacing:-.15px}

/* right sidebar */
.photo-box{left:835px;top:461px;width:250px;height:162px;border:1px solid var(--border);border-radius:4px}
.thumb{position:absolute;width:74px;height:62px;border:3px solid #ddd}
.view-more{position:absolute;right:6px;bottom:5px;font-size:7px;font-weight:700;color:var(--navy)}
.ad{left:834px;width:252px;border-radius:5px;border:1px solid #aac;overflow:hidden}
.ad-france{top:633px;height:165px;background:linear-gradient(#1c3e8c,#3a6fc0 45%,#c89a4a 65%,#2b3e6a 75%)}
.ad-band{position:absolute;left:0;bottom:0;width:100%;height:43px;background:#4f86c6;color:var(--white);padding:7px 11px;font-family:"PT Sans",sans-serif;font-weight:700;font-size:13px;line-height:15px}
.ad-yacht{top:810px;height:100px;background:linear-gradient(#fff 0,#fff 42px,#7fb8e6 44px,#2a6db3 100%)}
.ad-yacht h3{font-family:"PT Sans",sans-serif;font-size:17px;color:#7d1e6e;padding:3px 14px 0}
.ad-yacht p{font-size:8px;font-weight:700;color:var(--navy);text-align:right;padding-right:14px}
</style>
</head>
<body>

<header>
  <div class="abs hero"></div>
  <div class="abs hero-scene" role="img" aria-label="Photo de la tour Eiffel au bord de la Seine avec feuillage d'automne"></div>
  <div class="abs logo"><span class="logo-name">tourdepays.com</span><span class="logo-tag">portail de France</span></div>
  <nav class="abs top-links"><a href="#">/tourdepays.com</a> / <a href="#">Contact</a> /</nav>
  <form class="abs search">
    <div class="search-field">Search</div>
    <div class="search-btn"><svg width="14" height="14" viewBox="0 0 14 14"><circle cx="5.5" cy="5.5" r="3.8" fill="none" stroke="#fff" stroke-width="1.8"/><line x1="8.3" y1="8.3" x2="12.5" y2="12.5" stroke="#fff" stroke-width="2.2"/></svg></div>
  </form>
  <div class="abs polaroid" style="left:497px;top:46px;width:92px;height:146px"><div style="background:linear-gradient(#8fb4d8,#c99a6d 55%,#7a3a2a)" role="img" aria-label="Photo de maisons à colombages"></div></div>
  <div class="abs polaroid" style="left:576px;top:60px;width:124px;height:145px;transform:rotate(3deg)"><div style="background:linear-gradient(#4d90d6,#2a66b0 60%,#d8c6a2)" role="img" aria-label="Photo aérienne d'une ville côtière"></div></div>
  <div class="abs polaroid" style="left:675px;top:62px;width:125px;height:150px;transform:rotate(8deg)"><div style="background:radial-gradient(circle,#f5c458 0,#8a4b20 45%,#120c0a 80%)" role="img" aria-label="Photo d'une grande roue illuminée de nuit"></div></div>
  <div class="abs polaroid" style="left:786px;top:80px;width:140px;height:145px;transform:rotate(12deg)"><div style="background:radial-gradient(circle at 50% 60%,#f2c34c 0,#6d5a2a 40%,#0d1f66 75%)" role="img" aria-label="Photo de l'Arc de Triomphe de nuit"></div></div>

  <div class="abs city-strip">
    <span class="arrow" style="left:12px;border-right:8px solid var(--red)"></span>
    <div class="city" style="left:16px"><div class="crest" style="background:#7a3a5c" role="img" aria-label="Blason de Paris"></div>Paris</div>
    <div class="city" style="left:82px"><div class="crest" style="background:#b9c6e6" role="img" aria-label="Blason de Marseille"></div>Marseille</div>
    <div class="city" style="left:151px"><div class="crest" style="background:#8a3a4a" role="img" aria-label="Blason de Lyon"></div>Lyon</div>
    <div class="city" style="left:220px"><div class="crest" style="background:#a8324a" role="img" aria-label="Blason de Toulouse"></div>Toulouse</div>
    <div class="city" style="left:289px"><div class="crest" style="background:#d86a6a" role="img" aria-label="Blason de Nice"></div>Nice</div>
    <div class="city" style="left:352px"><div class="crest" style="background:#d88a8a" role="img" aria-label="Blason de Nantes"></div>Nantes</div>
    <div class="city" style="left:431px"><div class="crest" style="background:#ecc6c6" role="img" aria-label="Blason de Strasbourg"></div>Strasbourg</div>
    <div class="city" style="left:520px"><div class="crest" style="background:#6a7ab8" role="img" aria-label="Blason de Montpellier"></div>Montpellier</div>
    <div class="city" style="left:611px"><div class="crest" style="background:#9a3a5a" role="img" aria-label="Blason de Bordeaux"></div>Bordeaux</div>
    <div class="city" style="left:678px"><div class="crest" style="background:#d42a2a" role="img" aria-label="Blason de Lille"></div>Lille</div>
    <div class="city" style="left:742px"><div class="crest" style="background:#8a8a8a" role="img" aria-label="Blason de Rennes"></div>Rennes</div>
    <div class="city" style="left:818px"><div class="crest" style="background:#b04a40" role="img" aria-label="Blason du Havre"></div>Le Havre</div>
    <div class="city" style="left:890px"><div class="crest" style="background:#8a3a6a" role="img" aria-label="Blason de Reims"></div>Reims</div>
    <span class="arrow" style="left:962px;border-left:8px solid var(--red)"></span>
  </div>
  <div class="abs city-rule"></div>
</header>

<div class="abs crumb">tourdepays.com</div>

<aside>
  <h2 class="abs side-title" style="left:140px;top:435px">Les régions</h2>
  <nav class="abs regions">
    <span class="region">Alsace</span><span class="region">Aquitaine</span><span class="region">Auvergne</span>
    <span class="region">Basse-Normandie</span><span class="region">Bourgogne</span><span class="region">Bretagne</span>
    <span class="region">Centre</span><span class="region">Champagne-Ardenne</span><span class="region">Corse</span>
    <span class="region">Franche-Comté</span><span class="region">Haute-Normandie</span><span class="region">Île-de-France</span>
    <span class="region">Languedoc-Roussillon</span><span class="region">Limousin</span><span class="region">Lorraine</span>
    <span class="region">Midi-Pyrénées</span><span class="region">Nord-Pas-de-Calais</span>
  </nav>
</aside>

<main>
  <h1 class="abs section-title" style="left:358px;top:435px">Les villes de France</h1>
  <div class="abs intro-box"></div>
  <div class="abs map" role="img" aria-label="Carte colorée des régions de France"></div>
  <div class="abs intro-text">
    <p>&nbsp;Vous vous trouvez sur un site web dédié à vous donner toutes les informations dont vous avez besoin: Nous vous mettons à disposition une liste complète indiquant toutes les villes et tous les villages de France avec leurs codes postaux et des informations touristiques. Vous pouvez aussi télécharger les plus jolies photos de votre ville.</p>
    <p>En plus, vous trouvez ici des annonces immobilières qui vous aident à trouver la maison de vos rêves, des locaux appropriés pour votre nouveau bureau ou un petit appartement au centre-ville.</p>
    <p>Plusieurs informations supplémen­taires, comme le service de météo, la possibilité d'inscrire votre propre siteweb lié à votre ville et les actu­alités locaux, rendent complèt le total de notre offerte gratuite.</p>
  </div>

  <h2 class="abs section-title" style="left:358px;top:820px">Les plus belles villes du mois</h2>
  <div class="abs feature-box">La « capitale européenne » Strasbourg est aussi la capitale historique de l'Alsace à l'est de la France. Strasbourg compte 272 500 habitants et est aussi le chef-lieu du département Bas-Rhin. Au fil du développement de l'union européenne,</div>
</main>

<aside>
  <h2 class="abs section-title" style="left:841px;top:436px">Photo par hasard</h2>
  <div class="abs photo-box">
    <div class="thumb" style="left:6px;top:7px;background:linear-gradient(#6aa8e0,#2b7fc4 50%,#e6d29a)" role="img" aria-label="Photo de plage"></div>
    <div class="thumb" style="left:88px;top:7px;background:linear-gradient(#8a7a5a,#2fb0b8)" role="img" aria-label="Photo de crique"></div>
    <div class="thumb" style="left:168px;top:7px;background:linear-gradient(#7fb8e8,#d9c49a)" role="img" aria-label="Photo de village côtier"></div>
    <div class="thumb" style="left:6px;top:81px;background:linear-gradient(#4a86c8,#c9c9c9)" role="img" aria-label="Photo de port"></div>
    <div class="thumb" style="left:88px;top:81px;background:linear-gradient(#6fa0c0,#4fb6d8)" role="img" aria-label="Photo de piscine d'hôtel"></div>
    <div class="thumb" style="left:168px;top:81px;background:linear-gradient(#1f6aa8,#3ea0c8)" role="img" aria-label="Photo de baie"></div>
    <span class="view-more">View More</span>
  </div>
  <div class="abs ad ad-france" role="img" aria-label="Annonce : Paris de nuit au bord de la Seine">
    <div class="ad-band">FRANCE<br>Discover the “joie de vivre”</div>
  </div>
  <div class="abs ad ad-yacht" role="img" aria-label="Annonce : yacht en mer">
    <h3>Why charter a luxury yacht?</h3>
    <p>To find out, click here.</p>
  </div>
</aside>

</body>
</html>
```